Threadlane: fashion design product software needs your help

Fashion design product software company requests your assistance in designing a complete stationary package around our new logo design. Our software assists fashion designers and apparel houses with efficient communication and streamlined production between each other and manufacturers throughout the entire project design life cycle.

The look should reflect clean, simple and modern design. Not too "techie." Must use the provided logo and colors (or variations on the chosen colors, i.e. percentages as needed).

Reference website: www.threadlane-example.com

Buzzwords: manufacturing, production, apparel design/ers, streamlined process, effective communication, business, production software.

Please try to tone down or make the colors more subtle with more simple design style, layout. No sewing  theme. Thank you.

Target Market(s)

fashion designers and apparel houses that use software to manage and track production process life cycle.

Industry/Entity Type

Communication

Requirements
Must have
• Use of the logo and colors-or variations of colors (attached)
Nice to have
• Playfulness but corporate: with a sense of practicality, economical, streamlined production. Embossing considered.
Should not have
• Please keep in mind economics both financially and economically. Save trees and money! We believe in tactile paper but not "fashion-y" or sparkly, over-the-top colors, effects or production.

```html
<!DOCTYPE html>
<html lang="en">
<head>
<meta charset="utf-8">
<title>Threadlane Stationery</title>
<link rel="stylesheet" href="https://fonts.googleapis.com/css2?family=Ubuntu:wght@500&family=Open+Sans:wght@400;600&display=swap">
<style>
  :root {
    --board: #000000;
    --paper: #ffffff;
    --brand-blue: #35b0e2;
    --brand-blue-soft: #7ccbee;
    --brand-brown: #6e3520;
    --ink: #5a4034;
    --ink-light: #8a7a72;
  }
  * { margin: 0; padding: 0; box-sizing: border-box; }
  html, body { width: 1200px; height: 831px; overflow: hidden; background: var(--board); }
  .board { position: relative; width: 1200px; height: 831px; background: var(--board); font-family: "Open Sans", sans-serif; }

  .sheet { position: absolute; top: 50px; height: 729px; }
  .letterhead { left: 28px; width: 563px; background: var(--paper); }
  .letterhead-back { left: 609px; width: 563px; background: var(--brand-blue); }

  .wordmark { font-family: "Ubuntu", sans-serif; font-weight: 500; color: var(--brand-brown); letter-spacing: -0.5px; line-height: 1; position: absolute; }
  .letterhead .wordmark { left: 267px; top: 78px; font-size: 40px; }

  .contact { position: absolute; font-size: 7.5px; line-height: 10.5px; color: var(--ink); }
  .contact .label { color: var(--brand-blue); font-weight: 600; margin-right: 4px; }
  .contact .web { color: var(--ink-light); }
  .letterhead .contact { left: 400px; top: 130px; }

  .back-mark { position: absolute; left: 74px; top: 322px; font-family: "Ubuntu", sans-serif; font-weight: 500; font-size: 74px; color: var(--brand-blue-soft); letter-spacing: -1px; line-height: 1; }

  .card { position: absolute; left: 415px; width: 224px; height: 144px; box-shadow: 3px 4px 8px rgba(0,0,0,0.55); }
  .card-front { top: 439px; background: var(--paper); }
  .card-front .wordmark { left: 20px; top: 38px; font-size: 26px; }
  .card-front .contact { left: 118px; top: 84px; font-size: 6px; line-height: 8.5px; }
  .card-back { top: 593px; background: var(--brand-brown); }
  .card-back .contact { left: 118px; top: 82px; font-size: 6px; line-height: 8.5px; color: #e9d9cf; }
  .card-back .name { color: var(--brand-blue); font-weight: 600; }
  .card-back .gap { height: 8px; }
</style>
</head>
<body>
<main class="board">
  <section class="sheet letterhead">
    <div class="wordmark">Threadlane</div>
    <address class="contact">
      Threadlane Technologies Corp.<br>
      214 Loom Street<br>
      Hudson, NY 12534<br>
      <span class="label">t</span>555-014-2290<br>
      <span class="label">e</span>hello@threadlane-example.com<br>
      <span class="web">www.threadlane-example.com</span>
    </address>
  </section>

  <section class="sheet letterhead-back">
    <div class="back-mark">Threadlane</div>
  </section>

  <section class="card card-front">
    <div class="wordmark">Threadlane</div>
    <address class="contact">
      <strong>Threadlane Technologies Corp.</strong><br>
      214 Loom Street<br>
      Hudson, NY 12534<br>
      <span class="label">t</span>555-014-2290<br>
      <span class="label">e</span>hello@threadlane-example.com<br>
      <span class="web">www.threadlane-example.com</span>
    </address>
  </section>

  <section class="card card-back">
    <address class="contact">
      <span class="name">Dana Whitford</span><br>
      Director of Development<br>
      Threadlane Technologies Corp.<br>
      <div class="gap"></div>
      <span class="label">t</span>555-014-2290<br>
      <span class="label">e</span>dana@threadlane-example.com
    </address>
  </section>
</main>
</body>
</html>
```